Comparison Website Design for Glue Website

Note: We don't have a logo, it's not needed. Just put placeholder.

We would like a website comparing A to B, simple elegant design, simplistic styling. Website is for helping people find the best glue to glue 2 things together. For example, Metal to wood, Metal to rubber, glass to fabric and so on. Select 2 options and be shown the best glue/adhesive for the job.

Purpose of the website:
Allowing someone to pick 2 materials they want to glue together, and showing them the best product for it. We want someone to select 2 materials like "Metal and Rubber". It'll then show the best glues/adhesives from best #1 to #5-10 other ones. The design is simple and doesn't need much detail.

Design rules:
Please design using bootstrap 4 with a modified 1440px width.

We're looking for 4 main pages:
Home Page, Compare Page, Category Page, Product Page.

Target Market(s)

Everyone

Industry/Entity Type

Adhesive

Number of Pages Required

3 page

Font styles to use
Sans Serif

Colors
876aae
b7a5cd
6b449b
e4daeb
fefeff

Requirements
Must have
• We like the following features of these designs:
https://pixelvane.example/shots/6401517-CoverLoom-Dashboard - Main menu with the drop down, this will change depending on the active page. If they are on a metal page they could be shown "glue metal to ___" options. We also like the simple table view in this design under "users" heading.

https://pixelvane.example/shots/6300662-Volt-Sketch-Quotation-Page - The entire colour palette is great! The simplicity of the design is great.

https://pixelvane.example/shots/8593973-Loans-Comparison-UI - The boxes at the top look great, if there was 2 of these with a compare icon between them and above that saying "glue metal to rubber" and it shows an icon/image or metal and glue... The table of products is also good, it has dot points and details which we like.

https://pixelvane.example/shots/4586351-Transfer-Money/attachments/4586351-Transfer-Money?mode=media - The right it shows which 2 products are selected (metal and rubber) for example, on the left it would say "best glue for metal and rubber". This is too detailed though, so it would need to be simplified nicely.

https://linquora.example/ - They do a good job of "comparing" 2 things and displaying integrations well. You can get lots of ideas from them linking A to B similar to what we want to show.

https://www.campaignflowreview.example/leadnest-vs-drivemint/ - This shows a good example of the hero section how it should look.

Features of each page to help you design:
Home Page-
Menu (shown in examples above)
Hero section (colour section) with a centre heading saying "what do you want to glue together" with 2 boxes below to select materials from.
List of most popular searches (metal to rubber, glass to wood, fabric to leather... repeat these to fill space).
List of popular products with basic details about each one (grid format, not list).
FAQs - You choose design for this
Content section (simple design, headings, paragraphs, dotpoints, images...)
Blog section - Simple 3 column grid with an image on top, heading, paragraph, button.

Compare Page-
Showing 2 materials in the colour hero section under or to the right of the heading and paragraph.
Best product (highlighted)
9 other products (list table)
3 column section saying glue (product a to ___) with other product that isn't product b + reverse of this.
Content section

Category page-
heading and breadcrumbs in hero section
Standard product list 1 column on the left with filters, 3 products shown on the right in grid format with basic details on each one.

Product page-
Image left, details on the right.
Keep the image smaller not 50% as we want it to not take up too much space vertically.
Under this put a table where this product ranks for gluing things together. for example #3 for gluing metal to rubber, #1 for glass to wood.
Content section.

Please note, keep this design flat, simple and pretty. We don't need it over-designed or detailed, we simply want a simple functionality website that clearly shows what we're looking for.

```html
<!DOCTYPE html>
<html lang="en">
<head>
<meta charset="utf-8">
<title>Adhera Match – Home</title>
<link rel="stylesheet" href="https://fonts.googleapis.com/css2?family=Poppins:wght@400;500;600;700&display=swap">
<style>
:root{
  --hero:#582e8b;
  --band:#6f3fa6;
  --card-label:#8a62b4;
  --btn:#6b449b;
  --ink:#2f2f33;
  --body:#4a4a4f;
  --white:#fefeff;
  --grey:#e8e8e8;
  --line:#d2d2d6;
}
*{box-sizing:border-box;margin:0;padding:0}
html,body{width:1200px;height:3135px;overflow:hidden}
body{font-family:"Poppins",sans-serif;color:var(--ink);background:var(--white);position:relative}
section,header,footer{position:absolute;left:0;width:1200px}
.centre-title{position:absolute;left:0;width:100%;text-align:center;font-weight:600;font-size:34px;color:var(--ink);letter-spacing:-.3px}

/* header / hero */
.hero{top:0;height:477px;background:var(--hero);color:var(--white)}
.brand{position:absolute;left:159px;top:26px;font-size:24px;font-weight:500;letter-spacing:.5px;color:var(--white)}
.main-nav{position:absolute;top:33px;left:0;width:100%}
.main-nav a{position:absolute;font-size:12.5px;color:var(--white);text-decoration:none;font-weight:500}
.main-nav a.active::after{content:"";position:absolute;left:-2px;right:-2px;top:21px;height:2px;background:var(--white)}
.hero h1{position:absolute;top:130px;width:100%;text-align:center;font-size:29px;font-weight:700;letter-spacing:-.2px}
.material-pick{position:absolute;top:219px;width:155px;height:66px;border:2px solid var(--white);display:flex;align-items:center;justify-content:center;gap:10px;font-weight:600;font-size:17px;color:var(--white)}

/* searches */
.searches{top:477px;height:377px;background:var(--white)}
.search-card{position:absolute;width:338px;height:93px;border:1px solid var(--line);padding:16px 23px}
.search-card h3{font-size:16.5px;font-weight:500;color:var(--ink)}
.search-card p{font-size:13px;line-height:16px;color:var(--body);margin-top:6px;padding-left:1px}

/* products */
.products{top:854px;height:407px;background:var(--grey)}
.product-card{position:absolute;top:122px;width:188px;height:197px;box-shadow:0 2px 6px rgba(0,0,0,.12)}
.product-card .shot{height:133px}
.product-card .label{height:64px;background:var(--card-label);color:var(--white);display:flex;align-items:center;justify-content:center;font-size:16.5px;font-weight:500}

/* faq */
.faq{top:1261px;height:461px;background:var(--band);color:var(--white)}
.faq .centre-title{color:var(--white)}
.faq-q{position:absolute;left:388px;width:427px;font-size:14px;font-weight:600;color:var(--white)}
.faq-q span{position:absolute;right:0;top:-6px;font-size:24px;font-weight:400;color:var(--white)}
.faq-a{position:absolute;left:388px;top:1419px;width:400px;font-size:13.3px;line-height:18px;color:var(--white)}

/* blog */
.blog{top:1722px;height:620px;background:var(--white)}
.blog-card{position:absolute;top:130px;width:245px;height:415px;background:var(--white);box-shadow:0 2px 12px rgba(0,0,0,.13);padding:15px 10px}
.blog-card .shot{height:187px;border-radius:4px}
.blog-card h3{font-size:16.5px;line-height:19px;font-weight:600;margin:28px 8px 0;color:var(--ink)}
.blog-card p{font-size:13.5px;line-height:17px;margin:14px 8px 0;color:var(--body)}
.pill{display:inline-block;background:var(--btn);color:var(--white);border-radius:14px;font-size:12.5px;text-decoration:none;font-weight:500}
.blog-card .pill{margin:16px 8px 0;padding:5px 18px}

/* comparison */
.comparison{top:2342px;height:579px;background:var(--grey)}
.compare-row{position:absolute;left:214px;width:764px;height:83px;border-top:1px solid var(--line)}
.compare-row.last{border-bottom:1px solid var(--line)}
.compare-row h3{position:absolute;left:3px;top:23px;font-size:16.5px;line-height:19px;font-weight:600}
.compare-row p{position:absolute;left:268px;top:26px;font-size:13.5px;line-height:17px;color:var(--body);width:275px}
.compare-row .divider{position:absolute;left:652px;top:0;bottom:0;width:1px;background:#b8b8be}
.compare-row .pill{position:absolute;left:667px;top:24px;width:105px;height:35px;border-radius:18px;display:flex;align-items:center;justify-content:center;font-size:11.5px;font-weight:600}

/* footer */
.site-footer{top:2921px;height:214px;background:var(--band);color:var(--white)}
.site-footer .brand{left:90px;top:44px}
.foot-nav a{position:absolute;top:60px;font-size:12px;font-weight:600;color:var(--white);text-decoration:none}
.site-footer hr{position:absolute;left:89px;top:94px;width:1016px;border:0;border-top:1px solid rgba(255,255,255,.45)}
.follow{position:absolute;left:88px;top:132px;font-size:9.5px;font-weight:600;display:flex;align-items:center;gap:10px}
.follow i{display:inline-block;width:23px;height:23px;border-radius:50%;background:#9d7cc6}
.follow i:first-of-type{margin-left:4px}
.copyright{position:absolute;right:93px;top:134px;font-size:12px}
</style>
</head>
<body>

<header class="hero">
  <div class="brand">ADHERA MATCH</div>
  <nav class="main-nav">
    <a class="active" href="#" style="left:714px">HOME</a>
    <a href="#" style="left:781px">COMPARE</a>
    <a href="#" style="left:872px">CATEGORY</a>
    <a href="#" style="left:971px">PRODUCT</a>
  </nav>
  <h1>What do you want to glue together</h1>
  <div class="material-pick" style="left:434px">
    <svg width="38" height="30" viewBox="0 0 38 30" fill="none" stroke="#fefeff" stroke-width="2"><rect x="1" y="1" width="16" height="22"/><rect x="21" y="7" width="16" height="22"/><path d="M6 10h12M14 6l4 4-4 4M32 20H20M24 16l-4 4 4 4"/></svg>METAL
  </div>
  <div class="material-pick" style="left:604px">
    <svg width="38" height="30" viewBox="0 0 38 30" fill="none" stroke="#fefeff" stroke-width="2"><rect x="1" y="1" width="16" height="22"/><rect x="21" y="7" width="16" height="22"/><path d="M6 10h12M14 6l4 4-4 4M32 20H20M24 16l-4 4 4 4"/></svg>RUBBER
  </div>
</header>

<section class="searches">
  <h2 class="centre-title" style="top:43px">Most Popular Searches</h2>
  <div class="search-card" style="left:257px;top:116px"><h3>Metal to rubber</h3><p>Lrem ipsum dolor sit amcctetur<br>adipiscing elit, sed do</p></div>
  <div class="search-card" style="left:604px;top:116px"><h3>Glass to wood</h3><p>Lrem ipsum dolor sit amcctetur<br>adipiscing elit, sed do</p></div>
  <div class="search-card" style="left:257px;top:222px"><h3>Fabric to leather</h3><p>Lrem ipsum dolor sit amcctetur<br>adipiscing elit, sed do</p></div>
  <div class="search-card" style="left:604px;top:222px"><h3>Metal to rubber</h3><p>Lrem ipsum dolor sit amcctetur<br>adipiscing elit, sed do</p></div>
</section>

<section class="products">
  <h2 class="centre-title" style="top:46px">Popular products</h2>
  <div class="product-card" style="left:197px"><div class="shot" role="img" aria-label="Adhesive tube applied to a metal rail" style="background:linear-gradient(135deg,#9aa0a8,#7d7490 55%,#c9492f 80%,#2a3ea8)"></div><div class="label">Product name</div></div>
  <div class="product-card" style="left:403px"><div class="shot" role="img" aria-label="Sealant cartridge with nozzle" style="background:linear-gradient(135deg,#e8dcc4,#f4b23a 60%,#e59a12)"></div><div class="label">Product name</div></div>
  <div class="product-card" style="left:609px"><div class="shot" role="img" aria-label="Automated glue dispenser in a workshop" style="background:linear-gradient(160deg,#d9a73e,#6f6e74 50%,#2a2d33 85%,#c9541f)"></div><div class="label">Product name</div></div>
  <div class="product-card" style="left:814px"><div class="shot" role="img" aria-label="Hands holding a caulking gun" style="background:linear-gradient(135deg,#4a4b50,#7c5a44 50%,#d7d8dc 75%,#8a8c92)"></div><div class="label">Product name</div></div>
</section>

<section class="faq">
  <h2 class="centre-title" style="top:46px">Frequently Asked Questions</h2>
</section>
<div class="faq-q" style="top:1389px">Donec convallis pede venenatis?<span style="right:10px;top:-8px">-</span></div>
<p class="faq-a">parturient montes nascetur ridiculus mus In iaculis facilisis massa Etiam eu urna Sed porta Suspendisse quam</p>
<div class="faq-q" style="top:1490px">Nunc tempus felis vitae urna Vivamus porttitor ?<span>+</span></div>
<div class="faq-q" style="top:1549px">Curabitur iaculis tempus eros?<span>+</span></div>
<div class="faq-q" style="top:1608px">Morbi eget arcu Morbi porta libero ?<span>+</span></div>

<section class="blog">
  <h2 class="centre-title" style="top:60px">Latest Blog</h2>
  <article class="blog-card" style="left:202px"><div class="shot" role="img" aria-label="Applying adhesive along a wooden floor trim" style="background:linear-gradient(135deg,#6f4a2e,#a07652 55%,#c9c2bb 80%,#b5443a)"></div><h3>Sed ut perspiciatis unde omnis iste natusrsit</h3><p>Sed ut perspiciatis undemnis iste natus error sit voluptatem accusantium doloreme lau dantiumtotam rem</p><a class="pill" href="#">READ MORE</a></article>
  <article class="blog-card" style="left:477px"><div class="shot" role="img" aria-label="Worker sealing a frame with a caulking gun" style="background:linear-gradient(135deg,#f08a1c,#c3342b 45%,#2b2e3f 80%,#151820)"></div><h3>Sed ut perspiciatis unde omnis iste natusrsit</h3><p>Sed ut perspiciatis undemnis iste natus error sit voluptatem accusantium doloreme lau dantiumtotam rem</p><a class="pill" href="#">READ MORE</a></article>
  <article class="blog-card" style="left:753px"><div class="shot" role="img" aria-label="Robotic dispenser applying glue to a part" style="background:linear-gradient(135deg,#3d6fc7,#9cc3e8 50%,#dfe9f2 70%,#5a86c4)"></div><h3>Sed ut perspiciatis unde omnis iste natusrsit</h3><p>Sed ut perspiciatis undemnis iste natus error sit voluptatem accusantium doloreme lau dantiumtotam rem</p><a class="pill" href="#">READ MORE</a></article>
</section>

<section class="comparison">
  <h2 class="centre-title" style="top:64px">Latest Comparison</h2>
  <div class="compare-row" style="top:147px"><h3>Sed ut perspiciatis unde<br>omnis iste natusrsit</h3><p>Sed ut perspiciatis undemnis iste natus<br>sit voluptatem acclau dantiumtoem</p><span class="divider"></span><a class="pill" href="#">READ MORE</a></div>
  <div class="compare-row" style="top:230px"><h3>Sed ut perspiciatis unde<br>omnis iste natusrsit</h3><p>Sed ut perspiciatis undemnis iste natus<br>sit voluptatem acclau dantiumtoem</p><span class="divider"></span><a class="pill" href="#">READ MORE</a></div>
  <div class="compare-row" style="top:314px"><h3>Sed ut perspiciatis unde<br>omnis iste natusrsit</h3><p>Sed ut perspiciatis undemnis iste natus<br>sit voluptatem acclau dantiumtoem</p><span class="divider"></span><a class="pill" href="#">READ MORE</a></div>
  <div class="compare-row last" style="top:397px"><h3>Sed ut perspiciatis unde<br>omnis iste natusrsit</h3><p>Sed ut perspiciatis undemnis iste natus<br>sit voluptatem acclau dantiumtoem</p><span class="divider"></span><a class="pill" href="#">READ MORE</a></div>
</section>

<footer class="site-footer">
  <div class="brand">ADHERA MATCH</div>
  <nav class="foot-nav">
    <a href="#" style="left:768px">HOME</a>
    <a href="#" style="left:841px">COMPARE</a>
    <a href="#" style="left:946px">CATEGORY</a>
    <a href="#" style="left:1048px">PRODUCT</a>
  </nav>
  <hr>
  <div class="follow">FOLLOW US <i aria-label="Social link"></i><i aria-label="Social link"></i><i aria-label="Social link"></i></div>
  <div class="copyright">Copyright © 2020 All Rights Reserved</div>
</footer>

</body>
</html>
```